Compass & Canvas needs new business card design

I need a new business card design. I'm looking for out-of-the-box design which represents the freedom of being a location independent entrepreneur.
I offer coaching, retreats and trips.
I would like to see designs with and without the photo.
Colors I use are black (#000000), green (#25A796) and brown (#D7C38C)
Website compassandcanvas.net

Target Market(s)

location independent entrepreneurs, digital nomads, people looking to swap the 9 to 5 for a lifestyle business

Industry/Entity Type

Business

Contact Information for Business Card

Daria Tolsen
Your Lifestyle Business Coach, Retreat & Trip Leader
http://compassandcanvas.net
hello@compassandcanvas.net
Live a life you don't need a holiday from

Font styles to use
Serif
Sans Serif

Requirements
Must have
• One side should contain only the logo. I would also consider having the "Live a life you don't need a holiday from" on that side too (depending on how it looks)
• Please show both sides on the designs.

```html
<!DOCTYPE html>
<html lang="en">
<head>
<meta charset="utf-8">
<title>Compass &amp; Canvas – Business Card</title>
<link rel="stylesheet" href="https://fonts.googleapis.com/css2?family=Oswald:wght@400;500&family=PT+Sans+Narrow:wght@400;700&display=swap">
<style>
  :root {
    --page-bg: #e9e9e9;
    --teal: #0f9a86;
    --teal-deep: #078a79;
    --ink: #1f2022;
    --gold: #d7c38c;
    --white: #ffffff;
    --photo-light: #b8c2a4;
    --photo-mid: #7f9170;
    --photo-dark: #4d5d44;
  }
  * { box-sizing: border-box; margin: 0; padding: 0; }
  html, body { width: 1200px; height: 576px; overflow: hidden; }
  body {
    background: var(--page-bg);
    position: relative;
    font-family: "PT Sans Narrow", "Arial Narrow", sans-serif;
    color: var(--white);
  }
  .card {
    position: absolute;
    width: 484px;
    height: 291px;
    border-radius: 7px;
    overflow: hidden;
    box-shadow: 0 3px 6px rgba(0,0,0,0.25);
  }
  /* Front: logo side */
  .card-front {
    left: 82px; top: 139px;
    background: linear-gradient(180deg, var(--teal) 0%, var(--teal-deep) 100%);
  }
  .brand-name {
    position: absolute;
    left: 0; right: 0; top: 112px;
    text-align: center;
    font-family: "Oswald", sans-serif;
    font-weight: 400;
    font-size: 38px;
    letter-spacing: 1px;
    text-transform: uppercase;
    color: var(--white);
  }
  .front-web {
    position: absolute;
    left: 0; right: 0; top: 256px;
    display: flex;
    justify-content: center;
    align-items: center;
    gap: 12px;
    font-size: 13px;
  }
  .front-web .rule {
    width: 46px; height: 2px;
    background: var(--white);
    border-radius: 2px;
  }
  /* Back: details side */
  .card-back {
    left: 602px; top: 138px;
    width: 482px; height: 290px;
    background: var(--ink);
  }
  .photo-panel {
    position: absolute; inset: 0;
  }
  .person-name {
    position: absolute;
    left: 28px; top: 34px;
    font-family: "Oswald", sans-serif;
    font-weight: 500;
    font-size: 19px;
    letter-spacing: 0.3px;
    color: var(--gold);
    text-transform: uppercase;
  }
  .person-role {
    position: absolute;
    left: 28px; top: 61px;
    font-size: 12px;
    line-height: 14.5px;
  }
  .contact-list {
    position: absolute;
    left: 28px; top: 154px;
    list-style: none;
    font-size: 13px;
  }
  .contact-list li {
    display: flex;
    align-items: center;
    gap: 8px;
    height: 20.5px;
  }
  .contact-list svg { width: 11px; height: 11px; flex: none; }
  .social-mark {
    width: 10px; height: 10px;
    background: var(--teal);
    border-radius: 2px;
    flex: none;
  }
  .tagline-band {
    position: absolute;
    left: 0; top: 232px;
    width: 290px; height: 27px;
    background: var(--teal);
    padding-left: 28px;
    display: flex; align-items: center;
    font-size: 13.5px;
  }
</style>
</head>
<body>

  <section class="card card-front" aria-label="Business card front">
    <h1 class="brand-name">Compass &amp; Canvas</h1>
    <div class="front-web">
      <span class="rule"></span>
      <span>www.compassandcanvas.net</span>
      <span class="rule"></span>
    </div>
  </section>

  <section class="card card-back" aria-label="Business card back">
    <div class="tagline-band">Live a life you don't need a holiday from</div>

    <svg class="photo-panel" viewBox="0 0 482 290" width="482" height="290">
      <defs>
        <linearGradient id="photoTone" x1="0" y1="0" x2="0.4" y2="1">
          <stop offset="0" stop-color="var(--photo-light)"/>
          <stop offset="0.5" stop-color="var(--photo-mid)"/>
          <stop offset="1" stop-color="var(--photo-dark)"/>
        </linearGradient>
      </defs>
      <path d="M300 0 Q255 145 300 290 L482 290 L482 0 Z" fill="url(#photoTone)"
            role="img" aria-label="Photo of the coach sitting on a wooden rail among trees, holding a small sign"/>
      <path d="M293 -2 Q244 145 291 292" fill="none" stroke="var(--teal)" stroke-width="5"/>
    </svg>

    <h2 class="person-name">Daria Tolsen</h2>
    <p class="person-role">Your Lifestyle Business Coach,<br>Retreat Facilitator and Trip Leader</p>

    <ul class="contact-list">
      <li>
        <svg viewBox="0 0 12 12"><rect x="0.5" y="2" width="11" height="8" fill="var(--teal)"/><path d="M0.5 2 L6 6.5 L11.5 2" fill="none" stroke="var(--ink)" stroke-width="1"/></svg>
        <span>hello@compassandcanvas.net</span>
      </li>
      <li>
        <svg viewBox="0 0 12 12" fill="none" stroke="var(--teal)" stroke-width="1.2"><circle cx="6" cy="6" r="5"/><ellipse cx="6" cy="6" rx="2.2" ry="5"/><path d="M1 6 H11"/></svg>
        <span>www.compassandcanvas.net</span>
      </li>
      <li>
        <span class="social-mark"></span>
        <span>/compassandcanvas</span>
      </li>
    </ul>
  </section>

</body>
</html>
```